Homepage for preschool with coding and branding

Homepage for preschool

1. Homepage with:
- Large top section
- 3 columns below for the 3 main services
- A section to have an instagram feed of the school account
- Find / us map, contact info
- Footer

Standard header with menu
Standard footer

Please see current site

https://qlnk.example/7PRTvz4

New design must not be 'identical' to this.. must improve but match,

Target Market(s)

young moms in florida

Coding

Coded - Design and coding required

Number of Pages Required

2 page

Font styles to use
Sans Serif

Requirements
Must have
• - Match colors provided
- Match the 'style' of the logo across the site.

We use BuddyPress so must work with it.

```html
<!DOCTYPE html>
<html lang="en">
<head>
<meta charset="utf-8">
<title>Little Comets – Fun &amp; Safe Daycare</title>
<link rel="stylesheet" href="https://fonts.googleapis.com/css2?family=Rubik:wght@400;500;700;800&display=swap">
<style>
:root{
  --blue:#1a9ad6;
  --blue-dark:#0f7fb8;
  --yellow:#fde021;
  --navy:#14304a;
  --ink:#1c2b3a;
  --text:#3d4650;
  --dark:#2a2a2e;
  --footer:#173049;
  --white:#ffffff;
}
*{box-sizing:border-box;margin:0;padding:0}
html,body{width:1200px;height:4135px;overflow:hidden}
body{font-family:"Rubik",sans-serif;color:var(--text);background:var(--white)}
.page{position:relative;width:1200px;height:4135px;overflow:hidden}
.abs{position:absolute}
.btn{position:absolute;display:flex;align-items:center;justify-content:center;border-radius:30px;font-weight:500;text-decoration:none}
.btn-yellow{background:var(--yellow);color:var(--ink)}
.btn-blue{background:var(--blue);color:var(--white)}
.photo{position:absolute}
.brand{font-family:"Rubik",sans-serif;font-weight:800;color:var(--blue);display:flex;align-items:center;gap:8px;white-space:nowrap}
.brand-dot{width:18px;height:18px;border-radius:50%;background:var(--yellow)}

/* header */
.site-header{position:absolute;top:0;left:0;width:1200px;height:90px;background:var(--white);z-index:3}
.nav a{position:absolute;top:33px;font-size:17px;color:var(--ink);text-decoration:none}
.login{position:absolute;left:952px;top:25px;width:173px;height:40px;border:2px solid var(--blue);border-radius:22px;display:flex;align-items:center;justify-content:center;font-size:17px;color:var(--ink)}
.header-brand{position:absolute;left:510px;top:22px;font-size:26px}

/* hero */
.hero-photo{left:0;top:90px;width:1200px;height:720px;background:linear-gradient(135deg,#8a8f9a 0%,#5e6b7b 40%,#8c6c4e 75%,#3f6e9b 100%)}
.hero-title{left:0;top:330px;width:1200px;text-align:center;font-size:64px;font-weight:700;color:var(--white)}
.hero-sub{left:0;top:418px;width:1200px;text-align:center;font-size:20px;line-height:32px;color:var(--white)}
.arrow{position:absolute;width:50px;height:50px;border-radius:50%}

/* mission */
.h2{font-weight:800;color:var(--navy);text-transform:uppercase}
.mission-title{left:132px;top:872px;font-size:46px}
.mission-sub{left:132px;top:946px;width:420px;font-size:14px;line-height:21px;color:var(--ink)}
.mission-body{left:132px;top:1006px;width:440px;font-size:13px;line-height:24px}

/* services */
.service{position:absolute;border-radius:50%;display:flex;align-items:center;justify-content:center}
.service .img{width:100%;height:100%;border-radius:50%;display:flex;flex-direction:column;align-items:center;justify-content:flex-end;padding-bottom:52px;color:var(--white);font-weight:500;font-size:23px;letter-spacing:.5px}
.service .go{margin-top:10px;width:28px;height:28px;border-radius:50%;border:2px solid currentColor;display:flex;align-items:center;justify-content:center}

/* what we do */
.what-title{left:650px;top:1712px;font-size:44px;color:var(--white);font-weight:800}
.what-body{left:650px;top:1790px;width:430px;font-size:17px;line-height:24px;color:#e8e8ea}

/* questions */
.qa-title{font-size:32px;line-height:33px}
.qa-body{font-size:13px;line-height:19px;color:var(--ink)}

/* testimonials */
.testi-title{left:148px;top:2640px;font-size:44px;font-weight:700;color:var(--white)}
.dot{position:absolute;top:2724px;width:13px;height:13px;border-radius:50%;background:#cfe9f7}
.quote{left:698px;top:2614px;width:360px;font-size:17px;line-height:22px;color:var(--white)}
.quote-name{left:698px;top:2722px;font-size:17px;font-weight:500;color:var(--white)}

/* media */
.media-title{left:0;top:2905px;width:1200px;text-align:center;font-size:44px}

/* footer */
.foot-h{position:absolute;font-size:14px;font-weight:700;color:var(--white)}
.field{position:absolute;height:35px;background:var(--white);font-size:13px;color:#555;padding:10px 14px}
.links li{list-style:none;font-size:13px;color:#c8d6e2;height:27px;display:flex;align-items:center;gap:8px}
.links li::before{content:"»";color:var(--yellow);font-size:15px}
.contact li{list-style:none;font-size:13px;color:#c8d6e2;display:flex;gap:10px;margin-bottom:18px;line-height:19px}
.social{position:absolute;top:3962px;width:26px;height:26px;border-radius:50%;background:var(--white)}
.copyright{left:0;top:4091px;width:1200px;text-align:center;font-size:15px;color:#c8d6e2}
</style>
</head>
<body>
<div class="page">

  <!-- header -->
  <header class="site-header">
    <nav class="nav">
      <a style="left:98px">Mommy &amp; Me</a>
      <a style="left:245px">Mission</a>
      <a style="left:332px">Programes</a>
      <a style="left:738px">Gallery</a>
      <a style="left:820px">Contact Us</a>
    </nav>
    <div class="brand header-brand"><span class="brand-dot"></span>Little Comets</div>
    <div class="login">Members Login</div>
  </header>

  <!-- hero -->
  <div class="photo hero-photo" role="img" aria-label="Children playing with colourful building blocks in a classroom"></div>
  <svg class="abs" style="left:0;top:700px" width="1200" height="180" viewBox="0 0 1200 180">
    <path d="M0 60 C300 140 650 150 900 70 C1020 35 1120 20 1200 30 L1200 180 L0 180Z" fill="var(--blue)"/>
    <path d="M0 70 C300 150 650 160 900 80 C1020 45 1120 32 1200 42 L1200 180 L0 180Z" fill="var(--white)"/>
  </svg>
  <h1 class="abs hero-title">Fun &amp; Safe Daycare</h1>
  <p class="abs hero-sub">We offer high quality Daycare Services,<br>contact us or visit us today for more information</p>
  <a class="btn btn-yellow" style="left:505px;top:514px;width:187px;height:48px;font-size:19px">Learn More</a>
  <div class="arrow" style="left:73px;top:391px;border:2px solid var(--white)">
    <svg width="46" height="46" viewBox="0 0 46 46"><path d="M26 14 L17 23 L26 32" stroke="#fff" stroke-width="2.5" fill="none"/></svg>
  </div>
  <div class="arrow" style="left:1076px;top:391px;background:var(--blue)">
    <svg width="50" height="50" viewBox="0 0 50 50"><path d="M21 16 L30 25 L21 34" stroke="#fff" stroke-width="2.5" fill="none"/></svg>
  </div>

  <!-- mission -->
  <h2 class="abs h2 mission-title">Our Mission</h2>
  <p class="abs mission-sub">TO THE LITTLE COMETS MOMMY &amp; ME AND BRIGHT SPARKS PRESCHOOL PROGRAMS!</p>
  <p class="abs mission-body">Our fun, research-based educational classes provide interesting and varied experiences that are critical to children's social, mental and physical development. These comprehensive programs are taught in English and Spanish to provide early multilingual skills for an increasingly competitive multicultural world.</p>
  <div class="photo" style="left:655px;top:790px;width:420px;height:400px;border-radius:50%;background:radial-gradient(circle at 50% 45%,#f1c24a 0%,#e9a93a 30%,#2aa2dc 55%,#1a9ad6 100%)" role="img" aria-label="Smiling toddler in a yellow shirt playing with building blocks"></div>

  <!-- dark section -->
  <svg class="abs" style="left:0;top:1400px" width="1200" height="712" viewBox="0 0 1200 712">
    <path d="M0 190 C250 110 500 90 760 70 C950 55 1100 30 1200 0 L1200 712 L0 712Z" fill="var(--blue)"/>
    <path d="M0 200 C250 130 500 110 760 95 C950 85 1100 60 1200 25 L1200 712 L0 712Z" fill="var(--dark)"/>
  </svg>
  <div class="service" style="left:143px;top:1276px;width:304px;height:304px;background:var(--blue);padding:16px">
    <div class="img" style="background:linear-gradient(160deg,#e8b87a,#c8552e 60%,#6b8fb0)" role="img" aria-label="Child with painted hands making a heart shape">PROGRAMS<span class="go">›</span></div>
  </div>
  <div class="service" style="left:754px;top:1276px;width:304px;height:304px;background:var(--blue);padding:16px">
    <div class="img" style="background:linear-gradient(160deg,#9fb69a,#7b5a4a 55%,#4a6b88)" role="img" aria-label="Teacher reading with young children at a table">QUESTIONS?<span class="go">›</span></div>
  </div>
  <div class="service" style="left:433px;top:1259px;width:334px;height:334px;background:var(--yellow);padding:16px">
    <div class="img" style="background:linear-gradient(160deg,#d9d5cf,#9a7a6a 55%,#c44a3a)" role="img" aria-label="Group of cheering children in a playroom">CAMPS<span class="go" style="color:var(--yellow)">›</span></div>
  </div>
  <div class="photo" style="left:0;top:1676px;width:565px;height:436px;border-radius:0 70% 0 0;background:linear-gradient(140deg,#d8dde3,#e9a2b0 55%,#b7c7d8)" role="img" aria-label="Girl drawing at a desk in a bright classroom, video preview">
    <div class="abs" style="left:287px;top:165px;width:76px;height:76px;border-radius:50%;background:rgba(30,30,34,.85)">
      <svg width="76" height="76" viewBox="0 0 76 76"><path d="M31 24 L52 38 L31 52Z" fill="#fff"/></svg>
    </div>
  </div>
  <h2 class="abs what-title">WHT WE DO?</h2>
  <p class="abs what-body">Lorem Ipsum is simply dummy text of the printing and typesetting industry. Lorem Ipsum has been the industry's standard dummy text ever since the 1500s, when an unknown printer took a galley of type and scrambled it to make.</p>
  <a class="btn btn-yellow" style="left:650px;top:1935px;width:170px;height:44px;font-size:17px">Learn More</a>

  <!-- questions / covid -->
  <div class="photo" style="left:180px;top:2240px;width:165px;height:150px;border-radius:50%;background:radial-gradient(circle,#fde021 0%,#f5c800 70%,#e6e6e6 100%)" role="img" aria-label="Yellow question mark illustration"></div>
  <h2 class="abs h2 qa-title" style="left:374px;top:2205px">Got<br>Questions?</h2>
  <p class="abs qa-body" style="left:374px;top:2286px;width:250px">That's why we're here! Send us a note and we'll be more than happy to answer any questions you may have.</p>
  <a class="btn btn-blue" style="left:374px;top:2367px;width:153px;height:34px;font-size:14px">Send Us A Note</a>
  <div class="abs" style="left:651px;top:2205px;width:1px;height:205px;background:#d6d6d6"></div>
  <h2 class="abs h2 qa-title" style="left:693px;top:2203px">Covid-19 Update</h2>
  <p class="abs qa-body" style="left:693px;top:2256px;width:330px">Lorem Ipsum is simply dummy text of the printing and typesetting industry. Lorem Ipsum has been the industry's standard dummy text ever since the 1500s, when an unknown printer took.</p>
  <a class="btn btn-blue" style="left:695px;top:2367px;width:152px;height:34px;font-size:14px">Get Updates</a>

  <!-- testimonials -->
  <svg class="abs" style="left:0;top:2470px" width="1200" height="387" viewBox="0 0 1200 387">
    <path d="M0 50 C250 80 500 60 750 25 C950 0 1100 5 1200 25 L1200 387 L0 387Z" fill="var(--blue)"/>
  </svg>
  <h2 class="abs testi-title">TESTIMONIALS</h2>
  <span class="dot" style="left:271px"></span>
  <span class="dot" style="left:292px;background:var(--yellow)"></span>
  <span class="dot" style="left:313px"></span>
  <span class="dot" style="left:334px"></span>
  <div class="photo" style="left:546px;top:2606px;width:128px;height:128px;border-radius:50%;border:4px solid var(--white);background:linear-gradient(160deg,#e9e6e2,#b98a72 60%,#4b3a33)" role="img" aria-label="Portrait of a smiling parent"></div>
  <p class="abs quote">“&nbsp; Lorem Ipsum is simply dummy text the printing and typesetting industry. Lorem Ipsum has been the industry's standard dummy text ever since...”</p>
  <p class="abs quote-name">Name Heading</p>

  <!-- media -->
  <h2 class="abs h2 media-title">Our Media</h2>
  <div class="photo" style="left:142px;top:2983px;width:451px;height:382px;background:linear-gradient(150deg,#d9d6d2,#c4aa9a 50%,#c64a3d 80%,#3c6fb1)" role="img" aria-label="Children and parents dancing with a costumed bunny mascot"></div>
  <div class="photo" style="left:609px;top:2983px;width:252px;height:174px;background:linear-gradient(150deg,#5b6fc2,#d64a4a 50%,#f1c94a)" role="img" aria-label="Baby in a ball pit"></div>
  <div class="photo" style="left:878px;top:2983px;width:181px;height:174px;background:linear-gradient(150deg,#e5ddd5,#a98472 60%,#5f7fa6)" role="img" aria-label="Mothers with babies in a class"></div>
  <div class="photo" style="left:609px;top:3181px;width:170px;height:184px;background:linear-gradient(150deg,#7fb1d6,#d6a27a 55%,#2e79c2)" role="img" aria-label="Toddler crawling on a water play mat"></div>
  <div class="photo" style="left:796px;top:3181px;width:263px;height:184px;background:linear-gradient(150deg,#e7d8b5,#c9a57a 55%,#6aa15a)" role="img" aria-label="Children playing in a classroom"></div>

  <!-- map -->
  <div class="photo" style="left:0;top:3437px;width:1200px;height:230px;background:linear-gradient(135deg,#e6e9ec,#d9dee3 60%,#cfe0ea)" role="img" aria-label="Street map showing the school location"></div>

  <!-- footer -->
  <svg class="abs" style="left:0;top:3580px" width="1200" height="555" viewBox="0 0 1200 555">
    <path d="M0 30 C300 70 550 80 800 60 C980 45 1100 20 1200 0 L1200 555 L0 555Z" fill="var(--footer)"/>
  </svg>
  <div class="brand abs" style="left:520px;top:3665px;font-size:24px"><span class="brand-dot"></span>Little Comets</div>

  <h3 class="foot-h" style="left:135px;top:3760px">GET IN TOUCH</h3>
  <div class="field" style="left:132px;top:3810px;width:218px">Your kid's name</div>
  <div class="field" style="left:360px;top:3810px;width:220px">Your kid's age</div>
  <div class="field" style="left:132px;top:3857px;width:218px">Your Email</div>
  <div class="field" style="left:360px;top:3857px;width:220px">Phone Number</div>
  <div class="field" style="left:132px;top:3903px;width:448px;height:69px">Your Message</div>
  <a class="btn btn-blue" style="left:132px;top:3988px;width:130px;height:37px;font-size:16px">Send Us</a>

  <h3 class="foot-h" style="left:649px;top:3760px">QUICK LINKS</h3>
  <ul class="links abs" style="left:649px;top:3791px">
    <li>Mommy &amp; Me</li><li>Mission</li><li>Programes</li><li>Gallery</li><li>Contact Us</li>
  </ul>

  <h3 class="foot-h" style="left:834px;top:3760px">QUICK LINKS</h3>
  <ul class="contact abs" style="left:834px;top:3795px;width:260px">
    <li><svg width="14" height="18" viewBox="0 0 14 18"><path d="M7 1a6 6 0 0 0-6 6c0 4.5 6 10 6 10s6-5.5 6-10a6 6 0 0 0-6-6z" fill="none" stroke="var(--yellow)" stroke-width="1.5"/><circle cx="7" cy="7" r="2" fill="var(--yellow)"/></svg><span>LITTLE COMETS<br>THE MARKET AT PALM LAKE</span></li>
    <li><svg width="14" height="14" viewBox="0 0 14 14"><path d="M2 1h3l1.5 3.5-2 1.2a8 8 0 0 0 3.8 3.8l1.2-2L13 9v3a1 1 0 0 1-1 1A11 11 0 0 1 1 2a1 1 0 0 1 1-1z" fill="var(--yellow)"/></svg><span>(555) 014-2280</span></li>
    <li><svg width="15" height="12" viewBox="0 0 15 12"><rect x="1" y="1" width="13" height="10" fill="none" stroke="var(--yellow)" stroke-width="1.3"/><path d="M1 1l6.5 5.5L14 1" fill="none" stroke="var(--yellow)" stroke-width="1.3"/></svg><span>hello@littlecomets.example</span></li>
  </ul>

  <h3 class="foot-h" style="left:649px;top:3967px;font-size:13px">STAY CONNECTED</h3>
  <span class="social" style="left:800px"></span>
  <span class="social" style="left:834px"></span>
  <span class="social" style="left:868px"></span>
  <span class="social" style="left:904px"></span>

  <div class="abs" style="left:0;top:4065px;width:1200px;height:1px;background:#2f4862"></div>
  <p class="abs copyright">© 2020 Little Comets | All Rights are Reserved | Terms and Conditions</p>
</div>
</body>
</html>
```